metal roofing website

I have several domain names and a website that has been built. I need someone to recreate essentially the same website and change some photos and basic design to create the new sites. I have all of the files and c panel access to the lucky winner. If you can do a good job at a fair price I will have 100's of sites to send to you very soon. I have the site built and have all files just need it recreated on my server. the current site is www.brantlepanelinc.com I am looking to get this done ASAP!!!

```html
<!DOCTYPE html>
<html lang="en">
<head>
<meta charset="utf-8">
<title>Brantle Panel Inc. | Complete Post Frame and Garages</title>
<link href="https://fonts.googleapis.com/css2?family=Roboto:wght@700&family=Roboto+Condensed:wght@700&family=Montserrat:wght@400;500&family=Open+Sans:wght@400&display=swap" rel="stylesheet">
<style>
  :root {
    --brand-red: #b72f24;
    --header-beige: #e9dacb;
    --nav-text: #1e1e1e;
    --footer-bg: #2a3038;
    --white: #ffffff;
    --dot-idle: rgba(255,255,255,0.5);
    --hero-top: #a9aaa4;
    --hero-bottom: #6c7d58;
  }
  * { margin: 0; padding: 0; box-sizing: border-box; }
  html, body { width: 1200px; height: 742px; overflow: hidden; }
  body { position: relative; font-family: "Open Sans", sans-serif; background: var(--white); }

  .top-bar {
    position: absolute; left: 0; top: 0; width: 1200px; height: 42px;
    background: var(--brand-red);
  }
  .top-bar__phone {
    position: absolute; left: 798px; top: 11px;
    display: flex; align-items: center; gap: 6px; white-space: nowrap;
    font-family: "Roboto Condensed", sans-serif; font-weight: 700;
    font-size: 16px; color: var(--white);
  }
  .social { position: absolute; display: flex; gap: 18px; }
  .social__dot { width: 14px; height: 14px; border-radius: 50%; background: var(--white); }
  .top-bar .social { left: 992px; top: 14px; }

  .site-header {
    position: absolute; left: 0; top: 42px; width: 1200px; height: 111px;
    background: var(--header-beige);
  }
  .brand {
    position: absolute; left: 110px; top: 40px;
    display: flex; align-items: center; gap: 8px; white-space: nowrap;
    font-family: "Montserrat", sans-serif; font-weight: 500;
    font-size: 22px; color: var(--brand-red);
  }
  .brand__mark { width: 26px; height: 26px; background: var(--brand-red); }
  .main-nav__link {
    position: absolute; top: 55px; white-space: nowrap;
    font-family: "Montserrat", sans-serif; font-size: 12px; line-height: 16px;
    letter-spacing: 0.9px; color: var(--nav-text);
  }
  .main-nav__link--home { left: 514px; color: var(--brand-red); }
  .main-nav__link--about { left: 577px; }
  .main-nav__link--services { left: 667px; }
  .main-nav__link--gallery { left: 755px; }
  .main-nav__link--contact { left: 838px; }
  .btn-visualizer {
    position: absolute; left: 946px; top: 44px; width: 132px; height: 37px;
    border-radius: 19px; background: var(--brand-red); color: var(--white);
    font-family: "Montserrat", sans-serif; font-size: 12.5px; letter-spacing: 1px;
    display: flex; align-items: center; justify-content: center; white-space: nowrap;
  }

  .hero {
    position: absolute; left: 0; top: 153px; width: 1200px; height: 541px;
    background: linear-gradient(180deg, var(--hero-top) 0%, var(--hero-bottom) 100%);
  }
  .hero__title {
    position: absolute; left: 0; top: 178px; width: 1184px; text-align: center;
    font-family: "Roboto", sans-serif; font-weight: 700; font-size: 41px;
    line-height: 56px; color: var(--white);
  }
  .hero__cta {
    position: absolute; left: 527px; top: 317px; width: 129px; height: 46px;
    border: 2px solid var(--white); border-radius: 23px; color: var(--white);
    font-family: "Montserrat", sans-serif; font-size: 15px; white-space: nowrap;
    display: flex; align-items: center; justify-content: center;
  }
  .hero__arrow { position: absolute; top: 258px; }
  .hero__arrow--prev { left: 2px; }
  .hero__arrow--next { left: 1172px; }
  .hero__dots { position: absolute; left: 572px; top: 524px; display: flex; gap: 8px; }
  .hero__dot { width: 8px; height: 8px; border-radius: 50%; background: var(--dot-idle); }
  .hero__dot--active { background: var(--white); }

  .site-footer {
    position: absolute; left: 0; top: 694px; width: 1200px; height: 48px;
    background: var(--footer-bg);
  }
  .site-footer__copy {
    position: absolute; left: 106px; top: 15px; white-space: nowrap;
    font-size: 13px; color: var(--white);
  }
  .site-footer .social { left: 990px; top: 17px; gap: 20px; }
</style>
</head>
<body>
  <div class="top-bar">
    <div class="top-bar__phone">
      <svg width="11" height="17" viewBox="0 0 11 17" aria-hidden="true">
        <rect x="0.5" y="0.5" width="10" height="16" rx="2" fill="#fff"/>
        <rect x="2" y="2.5" width="7" height="10" fill="#b72f24"/>
        <circle cx="5.5" cy="14.5" r="1" fill="#b72f24"/>
      </svg>
      Call US: 715-555-0182
    </div>
    <div class="social" aria-label="Social links">
      <span class="social__dot"></span><span class="social__dot"></span><span class="social__dot"></span>
    </div>
  </div>

  <header class="site-header">
    <div class="brand"><span class="brand__mark"></span>Brantle Panel Inc</div>
    <nav class="main-nav">
      <span class="main-nav__link main-nav__link--home">HOME</span>
      <span class="main-nav__link main-nav__link--about">ABOUT US</span>
      <span class="main-nav__link main-nav__link--services">SERVICES</span>
      <span class="main-nav__link main-nav__link--gallery">GALLERY</span>
      <span class="main-nav__link main-nav__link--contact">CONTACT US</span>
    </nav>
    <span class="btn-visualizer">VISUALIZER</span>
  </header>

  <section class="hero" role="img" aria-label="Photo of a tan post frame house with dormers, porch and garage door on a green lawn">
    <h1 class="hero__title">Complete Post Frame<br>and Garages</h1>
    <span class="hero__cta">Contact Us</span>
    <svg class="hero__arrow hero__arrow--prev" width="14" height="26" viewBox="0 0 14 26" aria-hidden="true">
      <polyline points="12,2 2,13 12,24" fill="none" stroke="#fff" stroke-width="1.5"/>
    </svg>
    <svg class="hero__arrow hero__arrow--next" width="14" height="26" viewBox="0 0 14 26" aria-hidden="true">
      <polyline points="2,2 12,13 2,24" fill="none" stroke="#fff" stroke-width="1.5"/>
    </svg>
    <div class="hero__dots">
      <span class="hero__dot hero__dot--active"></span><span class="hero__dot"></span><span class="hero__dot"></span>
    </div>
  </section>

  <footer class="site-footer">
    <p class="site-footer__copy">Copyright © 2018 Brantle Panel Inc. All rights reserved.</p>
    <div class="social" aria-label="Social links">
      <span class="social__dot"></span><span class="social__dot"></span><span class="social__dot"></span>
    </div>
  </footer>
</body>
</html>
```